Historic Church website

We want our church website to feel warm, historic, and clean, modern, and easy to navigate. Dont use the anchor

Current website: https://www.meadowlarkfellowship.org/

Requirements
Should not have
• I would like to use the logo without the anchor

```html
<!DOCTYPE html>
<html lang="en">
<head>
<meta charset="utf-8">
<title>Meadowlark Fellowship</title>
<link href="https://fonts.googleapis.com/css2?family=Outfit:wght@300;400;500;600;700;800&display=swap" rel="stylesheet">
<style>
:root{
  --gold:#c8ad3c;
  --gold-deep:#b39a2e;
  --black:#0a0a0a;
  --charcoal:#1f1f1f;
  --cream:#f4ecdc;
  --white:#ffffff;
  --ink:#151515;
  --muted:#6b6b6b;
  --rule:#2b2b2b;
}
*{box-sizing:border-box;margin:0;padding:0}
html,body{width:1200px;height:4728px;overflow:hidden}
body{font-family:"Outfit",sans-serif;color:var(--ink);background:var(--white)}
.wrap{width:920px;margin:0 auto;position:relative;height:100%}
.btn{display:inline-block;font-size:13px;padding:12px 26px;text-decoration:none}
.btn-gold{background:var(--gold);color:var(--white)}
.btn-outline{border:1.5px solid var(--white);color:var(--white);padding:13px 40px}
.btn-dark-outline{border:1.5px solid var(--ink);color:var(--ink);padding:10px 24px;background:var(--white)}

/* hero */
.hero{height:688px;position:relative;background:
  radial-gradient(circle at 58% 34%,rgba(240,190,110,.55),rgba(0,0,0,0) 18%),
  radial-gradient(circle at 20% 70%,rgba(120,70,40,.5),rgba(0,0,0,0) 35%),
  linear-gradient(180deg,#2a1c14 0%,#3b281c 45%,#1a120c 100%)}
.hero-photo{position:absolute;inset:0}
.hero-shade{position:absolute;inset:0;background:rgba(0,0,0,.35)}
.nav{position:absolute;top:30px;left:140px;right:140px;display:flex;justify-content:space-between;align-items:center}
.brand{display:flex;align-items:center;gap:12px;color:var(--white);font-weight:600;font-size:19px}
.brand-dot{width:44px;height:44px;border-radius:50%;border:2px solid var(--white)}
.nav-links{display:flex;gap:26px;list-style:none}
.nav-links a{color:var(--white);text-decoration:none;font-size:15px}
.hero-copy{position:absolute;top:258px;left:0;right:0;text-align:center;color:var(--white)}
.hero-copy h1{font-size:44px;font-weight:800;line-height:1.12;letter-spacing:.5px}
.hero-copy .btn{margin-top:38px}

/* gold bands */
.band{height:184px;background:var(--gold);color:var(--white)}
.band .wrap{display:flex;align-items:center;justify-content:space-between}
.band h2{font-size:27px;font-weight:700;line-height:1.3}
.band-sermon{height:192px}

/* newsletter */
.newsletter{height:488px;background:var(--white)}
.newsletter .wrap{display:flex;padding-top:56px}
.news-photo{width:430px;height:380px;background:linear-gradient(135deg,#3a2a1f,#6b4a30 55%,#2a1d14)}
.news-form{width:490px;height:380px;background:var(--cream);padding:34px 44px}
.news-form h3{font-size:24px;font-weight:700;margin-bottom:16px}
.field label{display:block;font-size:13px;font-weight:600;margin-bottom:6px}
.field .input{background:var(--white);height:38px;font-size:11px;color:var(--muted);padding:12px 10px;margin-bottom:16px}
.news-form .btn{margin-top:4px}

/* about */
.about{height:592px;background:var(--black);color:var(--white)}
.about-copy{position:absolute;left:0;top:52px;width:460px;z-index:2}
.about-copy h2{font-size:27px;font-weight:700;line-height:1.28;margin-bottom:14px}
.about-copy p{font-size:13px;line-height:1.5;margin-bottom:14px;color:#e7e7e7}
.about-photo-a{position:absolute;left:492px;top:48px;width:296px;height:272px;background:linear-gradient(160deg,#5a3a22,#a77744 50%,#3b2616)}
.about-photo-b{position:absolute;left:628px;top:128px;width:292px;height:312px;background:radial-gradient(circle at 50% 55%,#f0b45a,#7a4016 35%,#1b0e07 80%);border:6px solid var(--black)}

/* visit */
.visit{height:616px;background:var(--charcoal);color:var(--white);text-align:center}
.visit h2{font-size:30px;font-weight:700;padding-top:52px}
.visit .sub{font-size:13px;margin-top:6px}
.visit-cards{display:flex;justify-content:space-between;margin-top:36px;text-align:left}
.visit-card{width:290px;height:328px;background:var(--white);color:var(--ink);padding:12px}
.visit-card .pic{height:200px;background:linear-gradient(160deg,#4a2c18,#b0783e 55%,#2b1a0e)}
.visit-card h3{font-size:17px;font-weight:700;margin-top:14px}
.visit-card .time{font-size:12px;margin-top:6px}
.visit-card .desc{font-size:11px;color:var(--muted);margin-top:6px;line-height:1.35}

/* events */
.events{height:544px;background:var(--cream)}
.events h2{text-align:center;font-size:30px;font-weight:700;padding-top:40px;margin-bottom:30px}
.event{display:flex;justify-content:space-between;align-items:center;height:80px;border-bottom:2px solid var(--ink);padding-top:14px}
.event-date{display:flex;align-items:baseline;gap:12px}
.event-date .day{font-size:52px;font-weight:700;line-height:1}
.event-date .month{font-size:14px}
.event-info{width:410px}
.event-info h3{font-size:24px;font-weight:700}
.event-info p{font-size:12px;margin-top:2px}
.events .more{text-align:center;margin-top:24px}

/* quote */
.quote{height:528px;background:var(--white)}
.quote-photo{position:absolute;left:20px;top:88px;width:290px;height:330px;border:7px solid var(--gold);border-radius:145px 145px 145px 0;background:linear-gradient(160deg,#2c1e15,#7b5634 55%,#1a110b)}
.quote-text{position:absolute;left:400px;top:120px;width:520px;color:var(--gold)}
.quote-text blockquote{font-size:22px;line-height:1.35}
.quote-text cite{display:block;font-style:normal;margin-top:22px;font-size:15px}
.quote-text cite strong{font-weight:700}

/* sermons */
.sermons{height:468px;background:var(--charcoal);color:var(--white)}
.sermons h2{text-align:center;font-size:30px;font-weight:700;padding-top:34px}
.sermon-cards{display:flex;justify-content:space-between;margin-top:26px}
.sermon-card{width:290px;height:338px;background:var(--white);color:var(--ink);padding:12px}
.sermon-card .pic{height:186px;background:linear-gradient(160deg,#3a2616,#a4723c 55%,#22160c)}
.sermon-card h3{font-size:18px;font-weight:700;line-height:1.2;margin-top:14px}
.sermon-card .date{font-size:12px;margin-top:6px}
.sermon-card .who{font-size:11px;color:var(--muted);margin-top:22px}

/* footer */
.footer{height:428px;background:var(--black);color:var(--white);text-align:center}
.footer .brand{justify-content:center;padding-top:40px}
.footer h2{font-size:28px;font-weight:700;margin-top:16px}
.footer .addr{font-size:13px;margin-top:14px;line-height:1.5}
.footer .line{font-size:13px;margin-top:8px}
.footer h4{font-size:18px;font-weight:700;margin-top:18px}
.socials{display:flex;justify-content:center;gap:10px;margin-top:12px}
.socials span{width:22px;height:22px;border-radius:50%;border:2px solid var(--white)}
.copyright{border-top:1px solid var(--rule);margin:24px 140px 0;padding-top:14px;font-size:12px}
</style>
</head>
<body>

<header class="hero">
  <div class="hero-photo" role="img" aria-label="Warmly lit historic library study with leather armchair, globe and tall bookshelves"></div>
  <div class="hero-shade"></div>
  <nav class="nav">
    <div class="brand"><span class="brand-dot"></span>Meadowlark Fellowship</div>
    <ul class="nav-links">
      <li><a href="#">About MFC</a></li>
      <li><a href="#">Ministries</a></li>
      <li><a href="#">Bible Studies</a></li>
      <li><a href="#">Sermon Library</a></li>
    </ul>
  </nav>
  <div class="hero-copy">
    <h1>ANCIENT CHURCH. ANCIENT FAITH.<br>ETERNAL TRUTH.</h1>
    <a class="btn btn-gold" href="#">Join our Community</a>
  </div>
</header>

<section class="band">
  <div class="wrap">
    <h2>We Have This Hope As An Anchor For The Soul<br>Firm And Secure Heb 6:19</h2>
    <a class="btn btn-outline" href="#">Get Direction</a>
  </div>
</section>

<section class="newsletter">
  <div class="wrap">
    <div class="news-photo" role="img" aria-label="Wood-panelled reading room with leather chair and bookshelves"></div>
    <form class="news-form">
      <h3>Sign Up For Our Weekly Newsletter</h3>
      <div class="field"><label>First Name</label><div class="input">Enter your first name</div></div>
      <div class="field"><label>Last Name</label><div class="input">Enter your last name</div></div>
      <div class="field"><label>Email</label><div class="input">Enter the email where you will receive our newsletter</div></div>
      <span class="btn btn-dark-outline">Click To Send</span>
    </form>
  </div>
</section>

<section class="about">
  <div class="wrap">
    <div class="about-photo-a" role="img" aria-label="Vaulted church interior with gilded arches"></div>
    <div class="about-photo-b" role="img" aria-label="Candle flames glowing in a dark sanctuary"></div>
    <div class="about-copy">
      <h2>Meadowlark Fellowship is an independent Christian church in the Protestant tradition.</h2>
      <p>Its central tenets are found in its Articles of Faith and include belief in the deity and lordship of Jesus Christ, the Trinity, Jesus' perfect life, atoning death on the cross, bodily resurrection, and ascension; Jesus' literal return; the inerrancy of the Bible in its original manuscripts; and our need for salvation through personal faith in Jesus Christ. In keeping with the prevailing perspective of the church during the centuries immediately following the Apostles, we teach Premillennialism.</p>
      <p>That is, the belief that Messiah will physically and literally return to earth at Jerusalem before the millennial age commences. At that time, he will establish a kingdom over which he will preside as King. All the promises of Israel's covenants will be literally fulfilled during this reign. At the end of one thousand years, the kingdom will be transferred from the Son to the Father (1 Cor 15:24-28) and it will merge with the eternal kingdom (Rev 20-21).</p>
    </div>
  </div>
</section>

<section class="band band-sermon">
  <div class="wrap">
    <h2>If You Cannot Join Us In Person Click Here<br>For This Week's Sermon</h2>
    <a class="btn btn-outline" href="#">Join Online</a>
  </div>
</section>

<section class="visit">
  <div class="wrap">
    <h2>Visit Us This Sunday</h2>
    <p class="sub">Flip The Boxes For More Information</p>
    <div class="visit-cards">
      <article class="visit-card">
        <div class="pic" role="img" aria-label="Candlelit worship sanctuary"></div>
        <h3>Morning Worship Service</h3>
        <p class="time">11:00 AM</p>
        <p class="desc">Sunday worship service and sermon takes place in the main sanctuary.</p>
      </article>
      <article class="visit-card">
        <div class="pic" role="img" aria-label="Long tables set for a shared church lunch"></div>
        <h3>All Church Lunch</h3>
        <p class="time">12:15 PM</p>
        <p class="desc">Please join us for lunch after the service. Everyone is welcome!</p>
      </article>
      <article class="visit-card">
        <div class="pic" role="img" aria-label="Open Bible on a wooden table in lamplight"></div>
        <h3>Afternoon Adult Bible Study</h3>
        <p class="time">12:45 PM</p>
        <p class="desc">TBA.</p>
      </article>
    </div>
  </div>
</section>

<section class="events">
  <div class="wrap">
    <h2>Upcoming MFC Events</h2>
    <div class="event">
      <div class="event-date"><span class="day">21</span><span class="month">January</span></div>
      <div class="event-info"><h3>7:30PM Wednesday Night Bible</h3><p>January 21, 2026 @ 7:30 pm – 8:30 pm</p></div>
    </div>
    <div class="event">
      <div class="event-date"><span class="day">25</span><span class="month">January</span></div>
      <div class="event-info"><h3>11:00AM Sunday Service</h3><p>January 25, 2026 @ 11:00 am – 12:15 pm</p></div>
    </div>
    <div class="event">
      <div class="event-date"><span class="day">1</span><span class="month">Feburary</span></div>
      <div class="event-info"><h3>11:00AM Sunday Service</h3><p>February 1 @ 11:00 am – 12:15</p></div>
    </div>
    <div class="event">
      <div class="event-date"><span class="day">4</span><span class="month">Feburary</span></div>
      <div class="event-info"><h3>7:30PM Wednesday Night Bible</h3><p>February 4 @ 7:30 pm – 8:30</p></div>
    </div>
    <div class="more"><a class="btn btn-gold" href="#">Read More</a></div>
  </div>
</section>

<section class="quote">
  <div class="wrap">
    <div class="quote-photo" role="img" aria-label="Preacher speaking to a congregation"></div>
    <div class="quote-text">
      <blockquote>We must meet the present situation, and we must speak a word to the world that no one else can speak. There are many reasons why we should do so. The need of the world, it's agony, it's pain, it's disease, call upon us to do so. But apart from that, it is our duty to do so.</blockquote>
      <cite><strong>Elias Harrow</strong>, Your Content Goes Here</cite>
    </div>
  </div>
</section>

<section class="sermons">
  <div class="wrap">
    <h2>MFC Sermons</h2>
    <div class="sermon-cards">
      <article class="sermon-card">
        <div class="pic" role="img" aria-label="Glowing lantern on a dark table"></div>
        <h3>Jesus Saves us from the Wrath to Come</h3>
        <p class="date">January 18, 2026</p>
        <p class="who">Meadowlark Fellowship</p>
      </article>
      <article class="sermon-card">
        <div class="pic" role="img" aria-label="Antique clock on a wall"></div>
        <h3>Jesus Saves us from the Wrath to Come</h3>
        <p class="date">January 18, 2026</p>
        <p class="who">Meadowlark Fellowship</p>
      </article>
      <article class="sermon-card">
        <div class="pic" role="img" aria-label="Bread and cup set for communion"></div>
        <h3>A New Song for a Renewed World</h3>
        <p class="date">January 11, 2026</p>
        <p class="who">Meadowlark Fellowship</p>
      </article>
    </div>
  </div>
</section>

<footer class="footer">
  <div class="brand"><span class="brand-dot"></span>Meadowlark Fellowship</div>
  <h2>Meadowlark Fellowship</h2>
  <p class="addr">2150 Larkspur Avenue<br>Fairhaven, California 90311</p>
  <p class="line"><strong>Phone:</strong> (310) 555-0187</p>
  <p class="line"><strong>Email:</strong> info@meadowlarkfellowship.org</p>
  <h4>Get Social</h4>
  <div class="socials"><span></span><span></span><span></span><span></span></div>
  <p class="copyright">© Copy Right 2026 | All Right Reserved</p>
</footer>

</body>
</html>
```